Quiet Harbor Candle Company needs a Label design

We need a label design for a new candle company based in Charleston South Carolina. Our mission is to provide people with candles that will fill any space with fragrances that are uplifting, comforting, fresh and will make any space feel like home. Our candles are aromatherapy, 100% soy wax, and hand poured (we would love for this to be indicated somewhere on the label). We would like to see a label that is modern, very clean and uses pastel colors like green, blush pink, mauve and blush blue. The final design should communicate peace, gratitude, hope, and happiness.

```html
<!DOCTYPE html>
<html lang="en">
<head>
<meta charset="utf-8">
<title>Honeysuckle Citrus Candle Label</title>
<link rel="stylesheet" href="https://fonts.googleapis.com/css2?family=Josefin+Sans:wght@300&family=Mrs+Saint+Delafield&family=Playfair+Display:wght@700&family=Playfair+Display+SC:wght@400&display=swap">
<style>
  :root {
    --ink: #2e2529;
    --page: #ffffff;
    --peach: #fbe7dc;
    --aqua: #d2faf8;
    --mint: #c4f8e5;
    --cream: #fbf5d4;
    --glow: #ffffff;
  }
  html, body {
    margin: 0;
    padding: 0;
    width: 1200px;
    height: 1102px;
    overflow: hidden;
    background: var(--page);
  }
  .label-canvas {
    position: relative;
    width: 1200px;
    height: 1102px;
  }
  .label-card {
    position: absolute;
    left: 137px;
    top: 181px;
    width: 919px;
    height: 695px;
    border-radius: 93px;
    background:
      radial-gradient(ellipse 38% 40% at 54% 52%, var(--glow) 0%, rgba(255,255,255,0) 100%),
      radial-gradient(ellipse 60% 60% at 0% 0%, var(--peach) 0%, rgba(251,231,220,0) 100%),
      radial-gradient(ellipse 60% 60% at 100% 0%, var(--aqua) 0%, rgba(210,250,248,0) 100%),
      radial-gradient(ellipse 60% 60% at 0% 100%, var(--mint) 0%, rgba(196,248,229,0) 100%),
      radial-gradient(ellipse 60% 60% at 100% 100%, var(--cream) 0%, rgba(251,245,212,0) 100%),
      #f7fbf6;
  }
  .label-type {
    position: absolute;
    inset: 0;
  }
  .logo-arc {
    font-family: "Josefin Sans", sans-serif;
    font-weight: 300;
    font-size: 34px;
    letter-spacing: 2px;
    text-transform: uppercase;
    fill: var(--ink);
  }
  .logo-word {
    font-family: "Playfair Display", serif;
    font-weight: 700;
    font-size: 88px;
    fill: var(--ink);
  }
  .scent-name {
    font-family: "Mrs Saint Delafield", cursive;
    font-size: 150px;
    fill: var(--ink);
  }
  .product-claims {
    font-family: "Playfair Display SC", serif;
    font-size: 40px;
    fill: var(--ink);
  }
</style>
</head>
<body>
<div class="label-canvas">
  <div class="label-card"></div>
  <svg class="label-type" width="1200" height="1102" viewBox="0 0 1200 1102" xmlns="http://www.w3.org/2000/svg">
    <defs>
      <path id="arc-top" d="M 522 264 Q 591 222 660 264" fill="none"/>
      <path id="arc-bottom" d="M 535 390 Q 597 432 664 384" fill="none"/>
    </defs>

    <text class="logo-arc"><textPath href="#arc-top" startOffset="50%" text-anchor="middle">Goes</textPath></text>
    <text class="logo-word" x="597" y="343" text-anchor="middle">LOGO</text>
    <text class="logo-arc"><textPath href="#arc-bottom" startOffset="50%" text-anchor="middle">Here</textPath></text>

    <text class="scent-name" x="237" y="504" textLength="741" lengthAdjust="spacingAndGlyphs">Honeysuckle</text>
    <text class="scent-name" x="384" y="669" textLength="420" lengthAdjust="spacingAndGlyphs">Citrus</text>

    <text class="product-claims" x="215" y="788" textLength="776" lengthAdjust="spacingAndGlyphs">Aromatherapy - Hand Poured  - 100% Soy Wax</text>
  </svg>
</div>
</body>
</html>
```